ガソリンスタンド店頭での自動車保険の販売を考えています。
保険商品は情報の非対称性が高く、ほとんどの顧客が自身の補償内容をよく把握しいません。また販売方の十分な説明ができていないケースも多いです。そこでよくある補償のミスマッチの例を挙げて保険の見直しを促していきたいと考えています。具体的なミスマッチは以下の三点です。

①車両保険について
車両保険のは一般と限定の二種類がありますが限定では自損事故や当て逃げの際の費用は補償されません。これを理解していない顧客は多いです。

②弁護士費用
任意保険に未加入の自動車ユーザーは地域によってだいぶ変わりますが全体の4割程度います。任意保険未加入の自動車と事故を起こした場合相手に過失がある場合でも物損であれば泣き寝入りするしかありません。また人身事故の場合でも自賠責の補償範囲を超す部分については自腹で清算する必要があります。弁護士を立て相手方と交渉することはできますが莫大な費用がかかります。
弁護士費用特約に加入していればこうした状況を回避することができます。費用的にも数百円程度の付加保険料で済みます。

③運転者限定
実際に運転をする方を限定することで、また年齢条件を設定することにより保険料の減額が見込めます。
しかし保険の組み方が複雑なため補償が受けられない、また過剰な補償となっている場合が数多くあります。

保険は敬遠されがちな分野ですので固くなりすぎず、親しみやすい雰囲気のPOPにしてもらえたらと思います。またPOPの種類や形状等も同時に提案してもらえれば助かります。「加入するかはどうか置いといて無駄や不足があるといけませんので一度補償内容の見直しをされませんか?」というスタイルで販売活動を進めていきますのでそれに沿ったPOPを作って欲しいと思います。
上記①②③に対応した保険会社のパンフレットを添付します。参考にしてください。
補足です。
当社調べでは他社契約分について、適正な補償内容になっていない方は8割程度いらっしゃいました。見た方が自分は大丈夫だろうかと注意喚起出来るような内容にして欲しいと思います。
自体や雰囲気ですが全体的に堅い印象のデザインが多かったのでもう少しポップな感じ、親しみやすい感じにしてほしいです。
すいません、延期させて頂きます。
延長します。
延期します…

やわらかいタッチで、誰が見てもわかりやすい内容でした。

ありがとうございました。

来年より、活用させていただきます。

ご提案いただきありがとうございました。

```html
<!DOCTYPE html>
<html lang="ja">
<head>
<meta charset="UTF-8">
<title>自動車保険 補償内容見直しPOP</title>
<link rel="stylesheet" href="https://fonts.googleapis.com/css2?family=M+PLUS+Rounded+1c:wght@700;800;900&family=Noto+Sans+JP:wght@400;700;900&display=swap">
<style>
  :root {
    --red: #e3221c;
    --deep-red: #9a1a14;
    --heart-a: #f9c878;
    --heart-b: #f08a5d;
    --ink: #2b2b2b;
    --body: #3a3a3a;
    --paper: #ffffff;
    --band: #e3221c;
    --accent-yellow: #ffe94a;
  }
  * { margin: 0; padding: 0; box-sizing: border-box; }
  html, body { width: 849px; height: 1200px; overflow: hidden; background: var(--paper); }
  .poster {
    position: relative;
    width: 849px;
    height: 1200px;
    background: var(--paper);
    font-family: "Noto Sans JP", sans-serif;
    color: var(--ink);
  }
  .category {
    position: absolute;
    top: 26px;
    right: 60px;
    font-size: 30px;
    font-weight: 700;
    color: var(--ink);
    letter-spacing: 2px;
  }
  .hero-art {
    position: absolute;
    left: 140px;
    top: 92px;
    width: 570px;
    height: 330px;
  }
  .headline {
    position: absolute;
    left: 0;
    top: 70px;
    width: 849px;
    font-family: "M PLUS Rounded 1c", sans-serif;
    font-weight: 900;
    line-height: 1;
    paint-order: stroke fill;
    -webkit-text-stroke: 10px var(--paper);
  }
  .headline .line1 {
    position: absolute;
    left: 66px;
    top: 10px;
    font-size: 108px;
    color: var(--red);
    letter-spacing: -2px;
    white-space: nowrap;
  }
  .headline .line2 {
    position: absolute;
    left: 112px;
    top: 138px;
    font-size: 102px;
    color: var(--deep-red);
    letter-spacing: -2px;
    white-space: nowrap;
  }
  .headline .hand {
    color: var(--red);
    font-size: 122px;
  }
  .stat {
    position: absolute;
    top: 330px;
    left: 0;
    width: 849px;
    text-align: center;
    font-family: "M PLUS Rounded 1c", sans-serif;
    font-weight: 800;
    font-size: 44px;
    color: var(--ink);
    white-space: nowrap;
    paint-order: stroke fill;
    -webkit-text-stroke: 6px var(--paper);
  }
  .stat .num-wrap {
    position: relative;
    display: inline-block;
    margin: 0 6px;
  }
  .stat .num {
    font-size: 96px;
    color: var(--red);
    font-weight: 900;
    vertical-align: -6px;
  }
  .stat .note {
    position: absolute;
    right: -62px;
    bottom: 4px;
    font-size: 12px;
    font-weight: 700;
    -webkit-text-stroke: 0;
  }
  .mismatch-band {
    position: absolute;
    top: 436px;
    left: 0;
    width: 849px;
    height: 50px;
    background: var(--band);
    color: var(--paper);
    font-weight: 900;
    font-size: 32px;
    text-align: center;
    line-height: 50px;
    letter-spacing: 1px;
  }
  .point {
    position: absolute;
    left: 60px;
  }
  .point h2 {
    font-size: 32px;
    font-weight: 900;
    color: var(--ink);
    line-height: 1.2;
    padding-bottom: 4px;
    border-bottom: 2px solid var(--ink);
    display: inline-block;
    padding-right: 16px;
  }
  .point p {
    margin-top: 10px;
    margin-left: 40px;
    font-size: 14px;
    line-height: 1.6;
    color: var(--body);
  }
  .point-vehicle { top: 514px; width: 520px; }
  .point-lawyer { top: 634px; width: 560px; }
  .point-driver { top: 860px; width: 740px; }
  .art { position: absolute; }
  .art-car { left: 590px; top: 500px; width: 210px; height: 140px; }
  .art-worry { left: 620px; top: 660px; width: 180px; height: 170px; }
  .art-accident { left: 640px; top: 830px; width: 150px; height: 80px; }
  .cta-band {
    position: absolute;
    left: 0;
    top: 1116px;
    width: 849px;
    height: 74px;
    background: var(--band);
    color: var(--paper);
    text-align: center;
    line-height: 74px;
    font-family: "M PLUS Rounded 1c", sans-serif;
    font-weight: 900;
    font-size: 38px;
    white-space: nowrap;
  }
  .cta-band .hand { color: var(--accent-yellow); font-size: 46px; }
</style>
</head>
<body>
<main class="poster">
  <div class="category">自動車保険</div>

  <svg class="hero-art" viewBox="0 0 570 330" role="img" aria-label="握手する手を包むハートのイラスト">
    <defs>
      <linearGradient id="heroFill" x1="0" y1="0" x2="1" y2="1">
        <stop offset="0" stop-color="var(--heart-a)"/>
        <stop offset="1" stop-color="var(--heart-b)"/>
      </linearGradient>
    </defs>
    <rect width="570" height="330" rx="24" fill="url(#heroFill)" opacity="0.75"/>
  </svg>

  <h1 class="headline">
    <span class="line1">安心の選択</span>
    <span class="line2">でき<span class="hand">手</span>ますか？</span>
  </h1>

  <div class="stat">何と！約<span class="num-wrap"><span class="num">80</span><span class="note">※当社調べ</span></span>%の方に</div>

  <div class="mismatch-band">補償内容のミスマッチがありました。</div>

  <section class="point point-vehicle">
    <h2>①車両保険について</h2>
    <p>車両保険には、一般と限定の二種類があります。<br>限定では自損事故や当て逃げの際の費用は補償されません。</p>
  </section>

  <svg class="art art-car" viewBox="0 0 210 140" role="img" aria-label="車が電柱にぶつかり困っている人のイラスト">
    <rect width="210" height="140" rx="10" fill="#f6e7a8"/>
  </svg>

  <section class="point point-lawyer">
    <h2>②弁護士費用について</h2>
    <p>知ってましたか？ 全体の４割の方は任意保険未加入です。もし、未加入の車と事故を起こした場合、相手に過失がある場合でも物損であれば泣き寝入りするしかありません。また人身事故の場合でも、自賠責の補償範囲を超えた部分については自腹で清算する必要があります。弁護士を立てて相手方と交渉することはできますが莫大な費用がかかります。弁護士費用特約に加入していればこうした状況を回避することができます。費用的にも数百円程度の付加保険料で済みます。</p>
  </section>

  <svg class="art art-worry" viewBox="0 0 180 170" role="img" aria-label="頭を抱えて悩むスーツ姿の男性のイラスト">
    <rect width="180" height="170" rx="10" fill="#e9e3da"/>
  </svg>

  <svg class="art art-accident" viewBox="0 0 150 80" role="img" aria-label="「事故」の文字を掲げたイラスト">
    <rect width="150" height="80" rx="8" fill="#f3d9d5"/>
  </svg>

  <section class="point point-driver">
    <h2>③運転者限定について</h2>
    <p>実際に運転をする方を限定、年齢条件を設定することで保険料の減額が見込めます。<br>保険の組み方が複雑なため補償が受けられない、また過剰な補償となっている場合が数多くあります。</p>
  </section>

  <div class="cta-band">当店スタッフと一緒に見直し<span class="hand">手</span>みませんか？</div>
</main>
</body>
</html>
```